Solvane Glow LED - E- Commerce site

We need a website designed for an LED Billboard company that sells:
1) LED Billboards (Sales & Rental)
2) LED Gas Station lights
3) Truss Systems (Sales & Rental)
4) Sound Systems (Sales & Rental)

Attached are websites that sell similar products as Solvane Glow LED. Target market is for business, property managers and event coordinators.
This site will need to be an e-commerce site where customers can purchase the product directly from the site. What I'm looking for is a design layout to start.

Conceptual Web Designs:
http://example-panelora.test/index.html
http://www.vormpix.com/
http://www.droneplayaudio.com/
http://www.quillmarkdisplay.com/

Attached is the logo of the company: Please note that the new spelling of the logo is "Solvane Glow LED" using domain " SolvaneGlowLED.com

Industry/Entity Type

Gas Station

Number of Pages Required

5+ page

Requirements
Must have
• 1) E-Commerce - Customers will need to be able to order product from the site.
• 2) Customers will also have the option to rent the product as well.
Nice to have
• I like the image of the attached website, that has a video clip loop
• http://www.quillmarkdisplay.com/

```html
<!DOCTYPE html>
<html lang="en">
<head>
<meta charset="utf-8">
<title>Solvane Glow LED</title>
<link href="https://fonts.googleapis.com/css2?family=Orbitron:wght@500;700&family=Open+Sans:wght@400;600;700&display=swap" rel="stylesheet">
<style>
:root{
  --yellow:#f2b418;
  --black:#141414;
  --ink:#222;
  --muted:#666;
  --light:#f0f0f0;
  --line:#dcdcdc;
  --white:#fff;
  --green:#4caf3a;
  --red:#e0262a;
  --teal:#1ea0b0;
  --purple:#8e1f78;
}
*{box-sizing:border-box;margin:0;padding:0}
html,body{width:1200px;height:2761px;overflow:hidden}
body{font-family:"Open Sans",Arial,sans-serif;color:var(--ink);background:var(--white);position:relative}
.wrap{width:876px;margin:0 auto;position:relative}

/* header */
.topbar{height:101px;background:var(--black);color:#eee;position:relative}
.brand{position:absolute;left:162px;top:22px;display:flex;align-items:center;gap:10px}
.brand-dot{width:50px;height:50px;border-radius:50%;border:5px solid var(--yellow)}
.brand-name{font-family:"Orbitron",sans-serif;font-weight:700;font-size:18px;color:var(--yellow);line-height:1.1;width:120px}
.toplinks{position:absolute;right:165px;top:14px;display:flex;gap:26px;font-size:11px;align-items:center}
.toplinks .phone{font-size:14px}
.toplinks .phone b{font-weight:700}
.search{position:absolute;left:666px;top:53px;display:flex}
.search input{width:202px;height:28px;border:0;padding:0 8px;font-size:10px;font-family:inherit}
.search button{width:30px;height:28px;background:var(--yellow);border:0;display:flex;align-items:center;justify-content:center}
.cart{position:absolute;left:920px;top:50px;display:flex;gap:8px;align-items:center;font-size:11px;line-height:1.4}
.cart-ic{width:32px;height:32px;border-radius:50%;background:var(--yellow);display:flex;align-items:center;justify-content:center}

.nav{height:50px;background:linear-gradient(#fafafa,#d6d6d6)}
.nav ul{list-style:none;display:flex;height:50px;width:876px;margin:0 auto}
.nav li{font-family:"Orbitron",sans-serif;font-weight:700;font-size:11.5px;letter-spacing:.5px;line-height:50px;padding:0 24px;color:#111}
.nav li.active{background:var(--yellow);color:#fff;padding:0 30px}

/* hero */
.hero{height:460px;position:relative;background:
  radial-gradient(ellipse 160px 240px at 10% 45%,rgba(230,120,60,.55),transparent 70%),
  radial-gradient(ellipse 140px 200px at 88% 55%,rgba(60,150,220,.5),transparent 70%),
  radial-gradient(ellipse 120px 180px at 50% 30%,rgba(240,200,120,.45),transparent 70%),
  radial-gradient(ellipse 140px 120px at 48% 78%,rgba(220,60,70,.5),transparent 70%),
  radial-gradient(ellipse 200px 260px at 72% 40%,rgba(120,160,220,.35),transparent 70%),
  linear-gradient(180deg,#3d5680 0%,#26344f 45%,#1a2236 100%)}
.hero h1{position:absolute;width:100%;top:172px;text-align:center;font-family:"Orbitron",sans-serif;font-weight:700;color:#fff;font-size:48px;line-height:54px;letter-spacing:2px;text-shadow:0 2px 10px rgba(0,0,0,.4)}
.hero h1 span{font-size:40px}
.hero .arrow{position:absolute;top:350px;width:32px;height:32px;border-radius:50%;border:1.5px solid #fff;display:flex;align-items:center;justify-content:center}

/* section titles */
.sec-title{display:flex;justify-content:center;align-items:center;gap:8px;font-family:"Orbitron",sans-serif;font-weight:700;font-size:22px;color:#444;letter-spacing:1px}
.sec-title .ring{width:30px;height:30px;border-radius:50%;border:4px solid var(--yellow)}
.sec-title em{font-style:normal;color:var(--yellow)}

/* welcome */
.welcome{height:447px;padding-top:30px}
.feature-row{display:flex;gap:19px;margin-top:30px}
.feature{width:279px}
.feature .pic{height:149px}
.pic-panel{background:radial-gradient(ellipse 90px 60px at 55% 40%,#ffffff,rgba(255,255,255,0) 80%),linear-gradient(180deg,#eef1ee 0%,#dfe4dc 60%,#9fae8e 100%)}
.pic-bulbs{background:radial-gradient(ellipse 70px 40px at 35% 40%,#f6f7f8,rgba(246,247,248,0) 80%),radial-gradient(ellipse 60px 40px at 70% 45%,#e9ecef,rgba(233,236,239,0) 80%),linear-gradient(180deg,#aebccb 0%,#c9d0d6 45%,#6f8257 80%,#4e5f3c 100%)}
.pic-station{background:radial-gradient(ellipse 120px 22px at 50% 42%,#ffffff,rgba(120,160,255,.6) 50%,rgba(20,30,80,0) 90%),radial-gradient(ellipse 110px 30px at 50% 72%,rgba(230,60,60,.8),rgba(230,60,60,0) 80%),linear-gradient(180deg,#070b1d 0%,#15204a 55%,#0c1226 100%)}
.feature h3{font-family:"Orbitron",sans-serif;font-size:13px;font-weight:700;margin-top:22px;letter-spacing:.5px}
.feature p{font-size:10.5px;color:var(--muted);line-height:17px;margin-top:14px}
.btn-more{display:inline-block;margin-top:18px;background:var(--yellow);color:#fff;font-family:"Orbitron",sans-serif;font-weight:700;font-size:10.5px;padding:10px 14px;width:120px}

/* product cards */
.newprod{height:466px;background:var(--light);padding-top:32px}
.card-row{display:flex;gap:17px}
.newprod .card-row{margin-top:31px}
.card{width:206px;height:309px;background:#fff;border:3px solid #fff;text-align:center;box-shadow:0 0 3px rgba(0,0,0,.08)}
.card .pic{height:144px;margin:4px}
.tone-silver{background:radial-gradient(ellipse 70px 48px at 50% 48%,#d9dcdf,#eeeff0 60%,#f7f7f7 100%)}
.tone-white{background:radial-gradient(ellipse 70px 44px at 50% 45%,#e4e6e8,#f6f6f6 65%,#ffffff 100%)}
.tone-dark{background:radial-gradient(ellipse 60px 40px at 50% 50%,#7b7f86,#d0d2d5 55%,#f4f4f4 100%)}
.tone-stage{background:radial-gradient(ellipse 76px 30px at 50% 30%,#c7c9cc,rgba(240,240,240,0) 80%),radial-gradient(ellipse 70px 30px at 50% 70%,#6a6e74,#e2e3e5 65%,#f3f3f3 100%)}
.card .price{color:var(--yellow);font-weight:700;font-size:14px;margin-top:14px}
.card h4{font-family:"Orbitron",sans-serif;font-size:11.5px;font-weight:700;margin-top:8px}
.card p{font-size:10px;color:var(--muted);line-height:15px;margin:8px 20px 0}
.actions{display:flex;gap:6px;justify-content:center;margin-top:13px}
.actions span{width:28px;height:28px;border-radius:50%;border:1.5px solid #ccc;display:flex;align-items:center;justify-content:center}
.actions span.buy{background:var(--yellow);border-color:var(--yellow)}
.card.hot{background:var(--yellow);border-color:var(--yellow)}
.card.hot .price,.card.hot h4,.card.hot p{color:#fff}
.card.hot .actions span{border-color:#fff;background:transparent}

/* why */
.why{height:405px;padding-top:54px}
.why-row{display:flex;margin-top:42px}
.why-item{width:175px;text-align:center}
.why-ic{width:86px;height:86px;border-radius:50%;border:4px solid;margin:0 auto;display:flex;align-items:center;justify-content:center}
.why-ic i{width:68px;height:68px;border-radius:50%;display:flex;align-items:center;justify-content:center}
.why-item h5{font-family:"Orbitron",sans-serif;font-size:12px;font-weight:500;letter-spacing:1px;margin-top:22px;color:#333}
.why-item p{font-size:10.5px;color:var(--muted);line-height:19px;margin:10px 14px 0}

/* catalogue */
.catalogue{height:519px;padding-top:38px;background:
  radial-gradient(ellipse 300px 120px at 20% 70%,rgba(200,208,200,.5),transparent 70%),
  radial-gradient(ellipse 260px 110px at 85% 60%,rgba(190,200,190,.5),transparent 70%),
  linear-gradient(#f5f6f7,#e6e9e8)}
.tabs{display:flex;justify-content:center;gap:8px;margin-top:20px}
.tabs span{font-family:"Orbitron",sans-serif;font-weight:500;font-size:12px;border:2px solid var(--line);background:#fff;color:#666;padding:9px 20px;letter-spacing:.5px}
.tabs span.on{background:var(--yellow);border-color:var(--yellow);color:#fff}
.catalogue .card-row{margin-top:26px}

/* footer */
.footer{height:252px;background:var(--black);color:#ddd;position:relative}
.footer h6{font-family:"Orbitron",sans-serif;font-size:11.5px;font-weight:700;color:#fff;letter-spacing:.5px}
.footer ul{list-style:none;font-size:10.5px;line-height:18px;margin-top:10px}
.f-brand{position:absolute;left:164px;top:28px;display:flex;align-items:center;gap:8px}
.f-brand .ring{width:66px;height:66px;border-radius:50%;border:5px solid #555}
.f-brand span{font-family:"Orbitron",sans-serif;font-weight:700;font-size:14px;color:#888;width:100px;line-height:1.2}
.f-col{position:absolute}
.news p{font-size:11px;margin-top:10px}
.news form{display:flex;margin-top:12px}
.news input{width:182px;height:30px;border:0;padding:0 10px;font-size:10px;font-style:italic;font-family:inherit}
.news button{width:79px;height:30px;border:0;background:var(--yellow);color:#fff;font-family:"Orbitron",sans-serif;font-weight:700;font-size:10.5px}
.social{display:flex;gap:8px;margin-top:12px}
.social span{width:30px;height:30px;border-radius:50%;border:1.5px solid #ccc}

.bottombar{height:61px;background:var(--yellow);display:flex;justify-content:space-between;align-items:center;padding:0 205px 0 166px;font-size:10px;color:#fff}
.bottombar nav{display:flex;gap:16px}
</style>
</head>
<body>

<header class="topbar">
  <div class="brand"><span class="brand-dot"></span><span class="brand-name">Solvane Glow LED</span></div>
  <div class="toplinks">
    <span class="phone">
      <svg width="12" height="12" viewBox="0 0 24 24" fill="#fff"><path d="M6.6 10.8a15 15 0 006.6 6.6l2.2-2.2c.3-.3.7-.4 1-.2 1.1.4 2.3.6 3.6.6.6 0 1 .4 1 1V20c0 .6-.4 1-1 1A17 17 0 013 4c0-.6.4-1 1-1h3.5c.6 0 1 .4 1 1 0 1.3.2 2.5.6 3.6.1.3 0 .7-.2 1z"/></svg>
      Phone: <b>0400 317 266</b></span>
    <span>Create Account</span>
    <span>Login ▾</span>
    <span>$ USD ▾</span>
    <span>English ▾</span>
  </div>
  <form class="search"><input placeholder="Enter a keyword..."><button type="button" aria-label="Search"><svg width="11" height="11" viewBox="0 0 24 24" fill="none" stroke="#fff" stroke-width="3"><circle cx="10" cy="10" r="7"/><path d="M15 15l6 6"/></svg></button></form>
  <div class="cart">
    <span class="cart-ic"><svg width="14" height="14" viewBox="0 0 24 24" fill="#fff"><path d="M2 3h3l3 11h10l3-8H7"/><circle cx="9" cy="19" r="2"/><circle cx="17" cy="19" r="2"/></svg></span>
    <span>SHOPPING CART<br>Items (0) - $0.00</span>
  </div>
</header>

<nav class="nav">
  <ul>
    <li class="active">HOME</li><li>ABOUT</li><li>OUR PRODUCTS</li><li>LED DISPLAYS</li><li>SOLUTION</li><li>GALLERY</li><li>CONTACT</li>
  </ul>
</nav>

<section class="hero" role="img" aria-label="Night city square lined with bright LED billboards">
  <h1>WE ARE AN LED<br><span>BILLBOARD COMPANY</span></h1>
  <span class="arrow" style="left:40px"><svg width="10" height="10" viewBox="0 0 10 10"><path d="M7 1L3 5l4 4" stroke="#fff" fill="none" stroke-width="1.5"/></svg></span>
  <span class="arrow" style="right:40px"><svg width="10" height="10" viewBox="0 0 10 10"><path d="M3 1l4 4-4 4" stroke="#fff" fill="none" stroke-width="1.5"/></svg></span>
</section>

<section class="welcome">
  <div class="wrap">
    <h2 class="sec-title"><span class="ring"></span>WELCOME TO SOLVANE GLOW <em>LED</em></h2>
    <div class="feature-row">
      <article class="feature">
        <div class="pic pic-panel" role="img" aria-label="Blank illuminated billboard panel"></div>
        <h3>LOREM IPSUM DOLOR SITETCO</h3>
        <p>Sd ut perspiciatis unde omnis isteiste natus error sit voluptatem accusantium doloremque lis5 ut perscialis unde omnis isteiste natus error sit vloreolu.</p>
        <span class="btn-more">READ MORE ›</span>
      </article>
      <article class="feature">
        <div class="pic pic-bulbs" role="img" aria-label="LED spotlight bulbs"></div>
        <h3>LOREM IPSUM DOLORITETCONS</h3>
        <p>Sd ut perspiciatis unde omnis isteiste natus error sit voluptatem accusantium doloremque lis5 ut perscialis unde omnis isteiste natus error sit vloreolu.</p>
        <span class="btn-more">READ MORE ›</span>
      </article>
      <article class="feature">
        <div class="pic pic-station" role="img" aria-label="Gas station canopy lit at night"></div>
        <h3>LOREM IPSUM DOLOR SETCONS</h3>
        <p>Sd ut perspiciatis unde omnis isteiste natus error sit voluptatem accusantium doloremque lis5 ut perscialis unde omnis isteiste natus error sit vloreolu.</p>
        <span class="btn-more">READ MORE ›</span>
      </article>
    </div>
  </div>
</section>

<section class="newprod">
  <div class="wrap">
    <h2 class="sec-title"><span class="ring"></span>NEW PRODUCTS</h2>
    <div class="card-row">
      <article class="card hot">
        <div class="pic tone-white" role="img" aria-label="Blank billboard frame"></div>
        <div class="price">$200.00</div><h4>PRODUCT NAME</h4>
        <p>Sed ut perspiciatis unde oml atus error sit voluptatem</p>
        <div class="actions"><span class="buy"><svg width="12" height="12" viewBox="0 0 24 24" fill="#fff"><path d="M2 3h3l3 11h10l3-8H7z"/></svg></span><span><svg width="12" height="12" viewBox="0 0 24 24" fill="#fff"><path d="M12 21l-8-8a5 5 0 017-7l1 1 1-1a5 5 0 017 7z"/></svg></span><span><svg width="12" height="12" viewBox="0 0 24 24" stroke="#fff" fill="none" stroke-width="2"><path d="M4 8h14l-3-3M20 16H6l3 3"/></svg></span></div>
      </article>
      <article class="card">
        <div class="pic tone-silver" role="img" aria-label="LED spotlight bulbs"></div>
        <div class="price">$200.00</div><h4>PRODUCT NAME</h4>
        <p>Sed ut perspiciatis unde oml atus error sit voluptatem</p>
        <div class="actions"><span class="buy"><svg width="12" height="12" viewBox="0 0 24 24" fill="#fff"><path d="M2 3h3l3 11h10l3-8H7z"/></svg></span><span><svg width="12" height="12" viewBox="0 0 24 24" fill="#bbb"><path d="M12 21l-8-8a5 5 0 017-7l1 1 1-1a5 5 0 017 7z"/></svg></span><span><svg width="12" height="12" viewBox="0 0 24 24" stroke="#bbb" fill="none" stroke-width="2"><path d="M4 8h14l-3-3M20 16H6l3 3"/></svg></span></div>
      </article>
      <article class="card">
        <div class="pic tone-stage" role="img" aria-label="Truss with stage lights"></div>
        <div class="price">$200.00</div><h4>PRODUCT NAME</h4>
        <p>Sed ut perspiciatis unde oml atus error sit voluptatem</p>
        <div class="actions"><span class="buy"><svg width="12" height="12" viewBox="0 0 24 24" fill="#fff"><path d="M2 3h3l3 11h10l3-8H7z"/></svg></span><span><svg width="12" height="12" viewBox="0 0 24 24" fill="#bbb"><path d="M12 21l-8-8a5 5 0 017-7l1 1 1-1a5 5 0 017 7z"/></svg></span><span><svg width="12" height="12" viewBox="0 0 24 24" stroke="#bbb" fill="none" stroke-width="2"><path d="M4 8h14l-3-3M20 16H6l3 3"/></svg></span></div>
      </article>
      <article class="card">
        <div class="pic tone-silver" role="img" aria-label="Illuminated sign box"></div>
        <div class="price">$200.00</div><h4>PRODUCT NAME</h4>
        <p>Sed ut perspiciatis unde oml atus error sit voluptatem</p>
        <div class="actions"><span class="buy"><svg width="12" height="12" viewBox="0 0 24 24" fill="#fff"><path d="M2 3h3l3 11h10l3-8H7z"/></svg></span><span><svg width="12" height="12" viewBox="0 0 24 24" fill="#bbb"><path d="M12 21l-8-8a5 5 0 017-7l1 1 1-1a5 5 0 017 7z"/></svg></span><span><svg width="12" height="12" viewBox="0 0 24 24" stroke="#bbb" fill="none" stroke-width="2"><path d="M4 8h14l-3-3M20 16H6l3 3"/></svg></span></div>
      </article>
    </div>
  </div>
</section>

<section class="why">
  <div class="wrap">
    <h2 class="sec-title"><span class="ring"></span>WHY CHOOSE SOLVANE GLOW <em>LED</em></h2>
    <div class="why-row">
      <div class="why-item"><div class="why-ic" style="border-color:var(--yellow)"><i style="background:var(--yellow)"><svg width="26" height="26" viewBox="0 0 24 24" fill="#fff"><path d="M12 2a7 7 0 00-4 12.7V17h8v-2.3A7 7 0 0012 2zM9 19h6v2H9z"/></svg></i></div><h5>TECHNOLOGY</h5><p>Sd ut perspiciatis unde is tenatus error sit volu pt at dol oremque lis5 ut perscialis ude omnis isteiste natus.</p></div>
      <div class="why-item"><div class="why-ic" style="border-color:var(--green)"><i style="background:var(--green)"><svg width="26" height="26" viewBox="0 0 24 24" fill="#fff"><path d="M3 3h9l9 9-9 9-9-9zM7 6a1.5 1.5 0 100 3 1.5 1.5 0 000-3z"/></svg></i></div><h5>PRICE</h5><p>Sd ut perspiciatis unde is tenatus error sit volu pt at dol oremque lis5 ut perscialis ude omnis isteiste natus.</p></div>
      <div class="why-item"><div class="why-ic" style="border-color:var(--red)"><i style="background:var(--red)"><svg width="26" height="26" viewBox="0 0 24 24"><circle cx="12" cy="12" r="7" fill="none" stroke="#fff" stroke-width="4" stroke-dasharray="3 2.5"/><circle cx="12" cy="12" r="3" fill="#fff"/></svg></i></div><h5>SERVICE</h5><p>Sd ut perspiciatis unde is tenatus error sit volu pt at dol oremque lis5 ut perscialis ude omnis isteiste natus.</p></div>
      <div class="why-item"><div class="why-ic" style="border-color:var(--teal)"><i style="background:var(--teal)"><svg width="26" height="26" viewBox="0 0 24 24" fill="#fff"><path d="M2 10h4v11H2zM8 21V10l5-8c2 0 3 1 2.5 3L14 9h6c1 0 2 1 1.7 2.3l-2 8c-.3 1-1 1.7-2 1.7z"/></svg></i></div><h5>QUALITY</h5><p>Sd ut perspiciatis unde is tenatus error sit volu pt at dol oremque lis5 ut perscialis ude omnis isteiste natus.</p></div>
      <div class="why-item"><div class="why-ic" style="border-color:var(--purple)"><i style="background:var(--purple)"><svg width="26" height="26" viewBox="0 0 24 24" fill="#fff"><path d="M12 2l8 3v6c0 5-3.5 9-8 11-4.5-2-8-6-8-11V5z"/></svg></i></div><h5>WARRANTY</h5><p>Sd ut perspiciatis unde is tenatus error sit volu pt at dol oremque lis5 ut perscialis ude omnis isteiste natus.</p></div>
    </div>
  </div>
</section>

<section class="catalogue">
  <div class="wrap">
    <h2 class="sec-title"><span class="ring"></span>SOLVANE GLOW <em>LED</em>&nbsp;PRODUCTS</h2>
    <div class="tabs"><span class="on">LED BILLBOARDS</span><span>TRUSSES</span><span>GAS STATION LIGHTS</span></div>
    <div class="card-row">
      <article class="card">
        <div class="pic tone-white" role="img" aria-label="Roadside billboard"></div>
        <div class="price">$200.00</div><h4>PRODUCT NAME</h4>
        <p>Sed ut perspiciatis unde oml atus error sit voluptatem</p>
        <div class="actions"><span class="buy"><svg width="12" height="12" viewBox="0 0 24 24" fill="#fff"><path d="M2 3h3l3 11h10l3-8H7z"/></svg></span><span><svg width="12" height="12" viewBox="0 0 24 24" fill="#bbb"><path d="M12 21l-8-8a5 5 0 017-7l1 1 1-1a5 5 0 017 7z"/></svg></span><span><svg width="12" height="12" viewBox="0 0 24 24" stroke="#bbb" fill="none" stroke-width="2"><path d="M4 8h14l-3-3M20 16H6l3 3"/></svg></span></div>
      </article>
      <article class="card">
        <div class="pic tone-white" role="img" aria-label="LED street light"></div>
        <div class="price">$200.00</div><h4>PRODUCT NAME</h4>
        <p>Sed ut perspiciatis unde oml atus error sit voluptatem</p>
        <div class="actions"><span class="buy"><svg width="12" height="12" viewBox="0 0 24 24" fill="#fff"><path d="M2 3h3l3 11h10l3-8H7z"/></svg></span><span><svg width="12" height="12" viewBox="0 0 24 24" fill="#bbb"><path d="M12 21l-8-8a5 5 0 017-7l1 1 1-1a5 5 0 017 7z"/></svg></span><span><svg width="12" height="12" viewBox="0 0 24 24" stroke="#bbb" fill="none" stroke-width="2"><path d="M4 8h14l-3-3M20 16H6l3 3"/></svg></span></div>
      </article>
      <article class="card">
        <div class="pic tone-silver" role="img" aria-label="Twin globe lamp post"></div>
        <div class="price">$200.00</div><h4>PRODUCT NAME</h4>
        <p>Sed ut perspiciatis unde oml atus error sit voluptatem</p>
        <div class="actions"><span class="buy"><svg width="12" height="12" viewBox="0 0 24 24" fill="#fff"><path d="M2 3h3l3 11h10l3-8H7z"/></svg></span><span><svg width="12" height="12" viewBox="0 0 24 24" fill="#bbb"><path d="M12 21l-8-8a5 5 0 017-7l1 1 1-1a5 5 0 017 7z"/></svg></span><span><svg width="12" height="12" viewBox="0 0 24 24" stroke="#bbb" fill="none" stroke-width="2"><path d="M4 8h14l-3-3M20 16H6l3 3"/></svg></span></div>
      </article>
      <article class="card">
        <div class="pic tone-dark" role="img" aria-label="LED display module"></div>
        <div class="price">$200.00</div><h4>PRODUCT NAME</h4>
        <p>Sed ut perspiciatis unde oml atus error sit voluptatem</p>
        <div class="actions"><span class="buy"><svg width="12" height="12" viewBox="0 0 24 24" fill="#fff"><path d="M2 3h3l3 11h10l3-8H7z"/></svg></span><span><svg width="12" height="12" viewBox="0 0 24 24" fill="#bbb"><path d="M12 21l-8-8a5 5 0 017-7l1 1 1-1a5 5 0 017 7z"/></svg></span><span><svg width="12" height="12" viewBox="0 0 24 24" stroke="#bbb" fill="none" stroke-width="2"><path d="M4 8h14l-3-3M20 16H6l3 3"/></svg></span></div>
      </article>
    </div>
  </div>
</section>

<footer class="footer">
  <div class="f-brand"><span class="ring"></span><span>Solvane Glow LED</span></div>
  <div class="f-col" style="left:162px;top:136px"><h6>ABOUT US</h6><ul><li>Company profile</li><li>News</li><li>Certification</li></ul></div>
  <div class="f-col" style="left:364px;top:30px"><h6>LED DISPLAY</h6><ul><li>Traffic Series</li><li>LED Mesh</li><li>Indoor High-Definition Series</li><li>Outdoor Fixed Series</li><li>Rental Indoor Series</li><li>Rental Outdoor Series</li><li>LCD Video Wall series</li><li>Wall Mounted Digital Signage</li><li>Floor Standing LCD Digital</li></ul></div>
  <div class="f-col" style="left:596px;top:30px"><h6>SUPPORT</h6><ul><li>Service Policy</li><li>Download Center</li><li>FAQ</li></ul>
    <h6 style="margin-top:22px">OTHERS</h6><ul><li>Solution</li><li>Gallery</li></ul></div>
  <div class="f-col news" style="left:775px;top:30px"><h6>SIGN UP NEWSLETTER</h6><p>Please sign up here for latest deals</p>
    <form><input placeholder="Email address"><button type="button">SIGN UP</button></form>
    <h6 style="margin-top:30px">FOLLOW US</h6>
    <div class="social"><span></span><span></span><span></span><span></span><span></span></div>
  </div>
</footer>

<div class="bottombar">
  <nav><span>Privacy statement</span><span>Use terms</span><span>Site Map</span></nav>
  <span>Copyright 2016 © Solvane Glow LED Ltd. ALL Rights Reserved</span>
</div>

</body>
</html>
```